Business card design needed

Mechanical services (heavy)
Training needs
Air conditioning (Automotive)
Parts Supplier

Industry/Entity Type

Automotive

Contact Information for Business Card

R T Mechanical Services
Colin Harwood (director)
47 Marlow Ridge highway
North Kelbrook W.A 6218
Mobile: 0417 563 904
rtmechanical4@mailvex.com

```html
<!DOCTYPE html>
<html lang="en">
<head>
<meta charset="utf-8">
<title>R T Mechanical Services – Business Card</title>
<link href="https://fonts.googleapis.com/css2?family=Arimo:wght@400;700&display=swap" rel="stylesheet">
<style>
  :root {
    --backdrop: #e9e9e9;
    --card: #fdfdfd;
    --brand-red: #c8202a;
    --brand-blue: #1a6fb8;
    --band-blue: #1570bd;
    --white: #ffffff;
    --card-shadow: rgba(0, 0, 0, 0.18);
  }
  * { box-sizing: border-box; margin: 0; padding: 0; }
  html, body {
    width: 1200px;
    height: 838px;
    overflow: hidden;
    background: var(--backdrop);
    font-family: "Arimo", Arial, sans-serif;
  }
  .sheet {
    position: relative;
    width: 1200px;
    height: 838px;
    display: flex;
    align-items: center;
    justify-content: center;
    gap: 40px;
  }
  .card {
    position: relative;
    width: 540px;
    height: 328px;
    background: var(--card);
    box-shadow: 0 6px 18px var(--card-shadow);
    overflow: hidden;
  }

  /* Front face */
  .contact-person { position: absolute; left: 30px; top: 30px; }
  .person-name {
    color: var(--brand-red);
    font-weight: 700;
    font-size: 19px;
  }
  .person-role {
    color: var(--brand-blue);
    font-size: 17px;
    margin-top: 2px;
  }
  .contact-details {
    position: absolute;
    left: 292px;
    top: 88px;
    color: var(--brand-blue);
    font-size: 17px;
    line-height: 1.5;
  }
  .contact-label { color: var(--brand-red); }
  .brand-lockup {
    position: absolute;
    left: 0;
    right: 0;
    top: 158px;
    display: flex;
    flex-direction: column;
    align-items: center;
  }
  .brand-dot {
    width: 52px;
    height: 52px;
    border-radius: 50%;
    background: var(--brand-blue);
  }
  .brand-name {
    margin-top: 8px;
    color: var(--brand-red);
    font-size: 20px;
  }
  .address-band {
    position: absolute;
    left: 0;
    right: 0;
    top: 250px;
    height: 34px;
    background: var(--band-blue);
    color: var(--white);
    font-size: 17px;
    line-height: 34px;
    padding-left: 24px;
    white-space: nowrap;
  }

  /* Back face */
  .card-back .brand-lockup {
    top: 92px;
  }
  .card-back .brand-dot {
    width: 100px;
    height: 100px;
  }
  .card-back .brand-name {
    margin-top: 14px;
    font-size: 24px;
  }
</style>
</head>
<body>
  <main class="sheet">
    <section class="card card-front">
      <div class="contact-person">
        <p class="person-name">Colin Harwood</p>
        <p class="person-role">Director</p>
      </div>
      <div class="contact-details">
        <p><span class="contact-label">Mobile:</span> 0417 563 904</p>
        <p>rtmechanical4@mailvex.com</p>
      </div>
      <div class="brand-lockup">
        <span class="brand-dot" aria-hidden="true"></span>
        <p class="brand-name">R T Mechanical</p>
      </div>
      <p class="address-band">47 Marlow Ridge highway, North Kelbrook, W.A 6218</p>
    </section>

    <section class="card card-back">
      <div class="brand-lockup">
        <span class="brand-dot" aria-hidden="true"></span>
        <p class="brand-name">R T Mechanical</p>
      </div>
    </section>
  </main>
</body>
</html>
```